Letterhead for clinic notes, test reports, and business cards

I need business card and letterheads for a medical clinic with the following:
1- Business cards. The back should allow for space for date and time of next appointments (few lines would do)
2- Letterhead for clinic notes
3- Letterhead for test reports.

Feel free to use whats included for examples. I value creativity so be creative.

Target Market(s)

Patients, referring physicians.

Industry/Entity Type

Health Care

Requirements
Must have
• Must use current logo.
• Must look good on white background
• Letterhead and reports must look good faxed.
• Please use themes of the current logo. Another possible color to use is grey as well (www.brackenvale-cardio.org - use the font color in the text of that website)

```html
<!DOCTYPE html>
<html lang="en">
<head>
<meta charset="utf-8">
<title>Brackenvale Heart Institute – Business Card</title>
<link href="https://fonts.googleapis.com/css2?family=Source+Sans+3:ital,wght@0,400;0,600;1,400&display=swap" rel="stylesheet">
<style>
  :root {
    --navy: #1c4a80;
    --deep-navy: #232a72;
    --blue: #1c7fc4;
    --red: #b81f2a;
    --grey-text: #5b5b5b;
    --rule: #c9c9c9;
    --backdrop: #e4e4e6;
    --card: #ffffff;
  }
  * { box-sizing: border-box; margin: 0; padding: 0; }
  html, body {
    width: 1105px; height: 1200px; overflow: hidden;
    background: var(--backdrop);
    font-family: "Source Sans 3", Arial, sans-serif;
  }
  .canvas { position: relative; width: 1105px; height: 1200px; }
  .card {
    position: absolute; left: 193px; width: 720px; height: 409px;
    background: var(--card);
  }
  .card--front { top: 168px; }
  .card--back { top: 623px; }

  /* Front */
  .brand-name {
    position: absolute; left: 40px; width: 312px; top: 140px;
    text-align: center; color: var(--navy);
    font-weight: 600; font-size: 34px; line-height: 1.1;
  }
  .divider {
    position: absolute; left: 360px; top: 73px; width: 1px; height: 228px;
    background: var(--rule);
  }
  .contact { position: absolute; left: 385px; top: 78px; }
  .contact__name { color: var(--navy); font-weight: 600; font-size: 28px; line-height: 1.2; }
  .contact__role { color: var(--red); font-size: 20px; line-height: 1.2; margin-bottom: 14px; }
  .contact__address, .contact__line {
    color: var(--grey-text); font-size: 19px; line-height: 1.4;
  }
  .contact__address { margin-bottom: 10px; }
  .contact__label { color: var(--navy); font-weight: 600; }
  .web-band {
    position: absolute; left: 0; top: 356px; width: 100%; height: 36px;
    background: linear-gradient(90deg, var(--deep-navy) 0%, var(--blue) 60%, var(--red) 88%, var(--red) 100%);
  }
  .web-band__url {
    position: absolute; left: 0; width: 680px; top: 0; line-height: 36px;
    text-align: center; color: #fff; font-size: 19px; letter-spacing: 3px;
  }
  .web-band__dot {
    position: absolute; right: 120px; top: 8px; width: 20px; height: 20px;
    border-radius: 50%; background: #fff;
  }

  /* Back */
  .appt-title {
    position: absolute; left: 0; width: 100%; top: 36px; text-align: center;
    color: var(--navy); font-size: 28px; font-weight: 400;
  }
  .field-label {
    position: absolute; color: var(--navy); font-size: 21px; line-height: 28px;
  }
  .dotted {
    position: absolute; height: 0; border-top: 1.5px dotted #7a7a7a;
  }
  .ampm { position: absolute; color: var(--navy); font-size: 16px; line-height: 28px; }
  .day { position: absolute; top: 197px; display: flex; align-items: center; gap: 6px;
    color: var(--navy); font-size: 19px; line-height: 28px; }
  .day__box { width: 18px; height: 18px; border: 1.5px solid #444; }
  .notice {
    position: absolute; left: 0; width: 100%; top: 334px; text-align: center;
    font-style: italic; color: var(--grey-text); font-size: 15px; line-height: 21px;
  }
</style>
</head>
<body>
<main class="canvas">
  <section class="card card--front">
    <div class="brand-name">Brackenvale Heart<br>Institute</div>
    <div class="divider"></div>
    <div class="contact">
      <p class="contact__name">Martin Hale</p>
      <p class="contact__role">CEO/Founder</p>
      <p class="contact__address">318 Corran Street, Suite 4B<br>Brackenvale ON K2P4M1</p>
      <p class="contact__line"><span class="contact__label">Phone:</span> 555-014-2287</p>
      <p class="contact__line"><span class="contact__label">Fax:</span> 555-014-2290</p>
      <p class="contact__line">contact@brackenvale-cardio.org</p>
    </div>
    <div class="web-band">
      <span class="web-band__url">www.brackenvale-cardio.org</span>
      <span class="web-band__dot"></span>
    </div>
  </section>

  <section class="card card--back">
    <h2 class="appt-title">Next Appointment</h2>

    <span class="field-label" style="left:44px; top:90px;">Name :</span>
    <span class="dotted" style="left:131px; top:112px; width:532px;"></span>

    <span class="field-label" style="left:44px; top:141px;">Date :</span>
    <span class="dotted" style="left:124px; top:163px; width:263px;"></span>
    <span class="field-label" style="left:394px; top:141px;">Time :</span>
    <span class="dotted" style="left:465px; top:163px; width:135px;"></span>
    <span class="ampm" style="left:609px; top:143px;">AM/PM</span>

    <span class="day" style="left:44px;">Sun <span class="day__box"></span></span>
    <span class="day" style="left:138px;">Mon <span class="day__box"></span></span>
    <span class="day" style="left:233px;">Tue <span class="day__box"></span></span>
    <span class="day" style="left:333px;">Wed <span class="day__box"></span></span>
    <span class="day" style="left:427px;">Thu <span class="day__box"></span></span>
    <span class="day" style="left:533px;">Fri <span class="day__box"></span></span>
    <span class="day" style="left:608px;">Sat <span class="day__box"></span></span>

    <span class="field-label" style="left:44px; top:244px;">Note :</span>
    <span class="dotted" style="left:128px; top:266px; width:535px;"></span>
    <span class="dotted" style="left:44px; top:302px; width:619px;"></span>

    <p class="notice">Please give me 24 hours notice if you are unable to keep your appointment or<br>a cancellation fee may be charged.</p>
  </section>
</main>
</body>
</html>
```